Ledgerwise Systems Group business card design.

We are a software development company that develop Software for finance companies and related industries.

We need a 2 sided business card designed. We have a new logo already designed (see attached eps and ai) We are after a clean simple corporate look. One side with just our logo, and the second side with our details.

Mark Hollister
Managing Director

Suite 4 Level 9, 138 Kellaway Street Sydney NSW 2000

Direct: +61 2 9374 6021
Mobile: +61 4 2287 5196
Email: markh@lsg-example.net.au
Web: www.lsg-example.net.au

I have included 2 logo files an .ai and .eps. I noticed that the lines either side of the group looks a bit jaggered and needs to be made sharper.

I would like to introduce a little colour somewhere rather than having it all black and white. But not over the top, keeping with a simple clean corporate look. Perhaps a light blue on some of the text?

If you have other ideas would be pleased to review

Regards

Mark H.

```html
<!DOCTYPE html>
<html lang="en">
<head>
<meta charset="utf-8">
<title>Ledgerwise Systems Group — Business Card</title>
<link rel="stylesheet" href="https://fonts.googleapis.com/css2?family=Titillium+Web:wght@300;400;700&display=swap">
<style>
  :root {
    --stage: #5e5e61;
    --card: #030304;
    --blue: #2aa6d6;
    --blue-deep: #1f8fc0;
    --white: #f4f6f8;
    --rule: #9a9ea3;
  }
  * { margin: 0; padding: 0; box-sizing: border-box; }
  html, body {
    width: 1200px;
    height: 873px;
    overflow: hidden;
  }
  body {
    background: var(--stage);
    font-family: "Titillium Web", "Helvetica Neue", Arial, sans-serif;
    position: relative;
  }
  .card {
    position: absolute;
    top: 278px;
    width: 520px;
    height: 316px;
    background: var(--card);
    overflow: hidden;
    box-shadow: 0 6px 18px rgba(0, 0, 0, 0.35);
  }
  .card--front { left: 50px; }
  .card--back { left: 630px; }

  /* shared brand lockup */
  .brand {
    position: absolute;
    display: flex;
    align-items: center;
    gap: 10px;
  }
  .brand__mark {
    width: 22px;
    height: 22px;
    background: var(--white);
    flex: none;
  }
  .brand__name {
    color: var(--blue);
    font-weight: 700;
    font-size: 15px;
    letter-spacing: 0.04em;
    text-transform: uppercase;
    line-height: 1;
    white-space: nowrap;
  }

  /* front side */
  .card--front .brand {
    left: 44px;
    top: 146px;
  }
  .front__band {
    position: absolute;
    top: 0;
    left: 372px;
    width: 46px;
    height: 100%;
    background: var(--blue);
  }

  /* back side */
  .card--back .brand {
    left: 30px;
    top: 100px;
  }
  .card--back .brand__name { font-size: 13px; }
  .back__rule {
    position: absolute;
    left: 288px;
    top: 111px;
    width: 158px;
    height: 1px;
    background: var(--rule);
  }
  .back__address {
    position: absolute;
    right: 58px;
    top: 26px;
    color: var(--blue);
    font-weight: 300;
    font-size: 9px;
    line-height: 1.5;
    text-align: right;
  }
  .back__band {
    position: absolute;
    top: 0;
    right: 26px;
    width: 14px;
    height: 100%;
    background: var(--blue-deep);
  }
  .person {
    position: absolute;
    left: 30px;
    top: 152px;
  }
  .person__name {
    color: var(--blue);
    font-weight: 300;
    font-size: 22px;
    line-height: 1.1;
  }
  .person__role {
    color: var(--white);
    font-weight: 400;
    font-size: 10px;
    margin-top: 2px;
  }
  .contacts {
    position: absolute;
    left: 30px;
    top: 218px;
    list-style: none;
  }
  .contacts__item {
    display: flex;
    align-items: center;
    gap: 8px;
    color: var(--white);
    font-weight: 300;
    font-size: 10px;
    height: 22px;
  }
  .contacts__icon {
    width: 14px;
    height: 14px;
    flex: none;
  }
</style>
</head>
<body>

  <section class="card card--front" aria-label="Business card front">
    <div class="brand">
      <span class="brand__mark" aria-hidden="true"></span>
      <span class="brand__name">Ledgerwise Systems Group</span>
    </div>
    <div class="front__band" aria-hidden="true"></div>
  </section>

  <section class="card card--back" aria-label="Business card back">
    <address class="back__address">
      Suite 4 Level 9, 138<br>
      Kellaway Street<br>
      Sydney NSW 2000
    </address>
    <div class="back__band" aria-hidden="true"></div>

    <div class="brand">
      <span class="brand__mark" aria-hidden="true"></span>
      <span class="brand__name">Ledgerwise Systems Group</span>
    </div>
    <div class="back__rule" aria-hidden="true"></div>

    <div class="person">
      <p class="person__name">Mark Hollister</p>
      <p class="person__role">Managing Director</p>
    </div>

    <ul class="contacts">
      <li class="contacts__item">
        <svg class="contacts__icon" viewBox="0 0 14 14" aria-hidden="true">
          <rect width="14" height="14" fill="#2aa6d6"/>
          <rect x="2.5" y="4" width="9" height="6.5" fill="none" stroke="#030304" stroke-width="1"/>
          <path d="M2.5 4 L7 8 L11.5 4" fill="none" stroke="#030304" stroke-width="1"/>
        </svg>
        <span>: markh@lsg-example.net.au</span>
      </li>
      <li class="contacts__item">
        <svg class="contacts__icon" viewBox="0 0 14 14" aria-hidden="true">
          <circle cx="7" cy="7" r="7" fill="#2aa6d6"/>
          <path d="M4.6 3.6 L6 3.4 L6.6 5.3 L5.7 6 Q6.5 7.8 8 8.4 L8.7 7.5 L10.6 8.1 L10.4 9.5 Q7.5 10.3 5.4 8 Q3.6 6 4.6 3.6 Z" fill="#030304"/>
        </svg>
        <span>: +61 4 2287 5196</span>
      </li>
      <li class="contacts__item">
        <svg class="contacts__icon" viewBox="0 0 14 14" aria-hidden="true">
          <circle cx="7" cy="7" r="7" fill="#2aa6d6"/>
          <circle cx="7" cy="7" r="4" fill="none" stroke="#030304" stroke-width="0.9"/>
          <ellipse cx="7" cy="7" rx="1.7" ry="4" fill="none" stroke="#030304" stroke-width="0.8"/>
          <path d="M3 7 H11" stroke="#030304" stroke-width="0.8"/>
        </svg>
        <span>: www.lsg-example.net.au</span>
      </li>
    </ul>
  </section>

</body>
</html>
```